Oil and Gas Exploration and Production company needs a business card design

We need a business card design using our logo and colors in the logo. We want a mainstream design.

```html
<!DOCTYPE html>
<html lang="en">
<head>
<meta charset="utf-8">
<title>Sunvale Oil &amp; Gas — Business Card</title>
<link rel="stylesheet" href="https://fonts.googleapis.com/css2?family=Merriweather:wght@400;900&display=swap">
<style>
  :root {
    --stage: #2a2b2e;
    --card-white: #ffffff;
    --card-black: #0d0d0d;
    --gold: #d9a530;
    --ink: #111111;
    --muted: #333333;
  }
  * { box-sizing: border-box; margin: 0; padding: 0; }
  html, body { width: 1200px; height: 900px; overflow: hidden; }
  body {
    background: var(--stage);
    font-family: "Merriweather", Georgia, serif;
    position: relative;
  }
  .card {
    position: absolute;
    width: 504px;
    height: 288px;
    border-radius: 22px;
    overflow: hidden;
    box-shadow: 0 18px 40px rgba(0,0,0,.45);
  }
  /* Front */
  .card-front { left: 68px; top: 306px; background: var(--card-white); }
  .contact { position: absolute; left: 34px; top: 30px; }
  .contact .person-name {
    color: var(--gold); font-size: 17px; font-weight: 400; letter-spacing: .3px;
  }
  .contact .person-role { font-size: 12px; color: var(--muted); margin-top: 4px; }
  .contact .address { font-size: 12.5px; color: var(--ink); margin-top: 24px; line-height: 1.5; }
  .contact .line {
    display: flex; align-items: center; gap: 10px;
    font-size: 12.5px; color: var(--ink); margin-top: 8px;
  }
  .contact .line svg { width: 14px; height: 14px; fill: var(--gold); flex: none; }
  .contact .address + .line { margin-top: 16px; }

  .brand {
    position: absolute; display: flex; align-items: center; gap: 10px;
    font-weight: 900; line-height: 1;
  }
  .brand .brand-dot { border-radius: 50%; background: var(--gold); flex: none; }
  .card-front .brand { right: 36px; top: 112px; color: var(--ink); font-size: 26px; }
  .card-front .brand .brand-dot { width: 20px; height: 20px; }

  .edge-band {
    position: absolute; left: 0; bottom: 0; width: 100%; height: 44px;
    background: var(--card-black);
  }
  .edge-rule {
    position: absolute; left: 0; bottom: 50px; width: 46%; height: 2px;
    background: var(--card-black);
  }
  .web-tab {
    position: absolute; right: 0; bottom: 0; width: 54%; height: 44px;
    background: var(--gold); border-top-left-radius: 26px;
    display: flex; align-items: center; padding-left: 34px;
    font-size: 14px; color: var(--ink);
  }

  /* Back */
  .card-back { left: 628px; top: 306px; background: var(--card-black); }
  .card-back .brand {
    left: 50%; top: 50%; transform: translate(-50%, -50%);
    color: var(--card-white); font-size: 34px;
  }
  .card-back .brand .brand-dot { width: 26px; height: 26px; }
</style>
</head>
<body>
  <section class="card card-front" aria-label="Business card front">
    <div class="contact">
      <p class="person-name">JOHNATHAN DOE</p>
      <p class="person-role">owner</p>
      <p class="address">Address Line 1<br>Place Name, NJ 45574</p>
      <p class="line">
        <svg viewBox="0 0 24 24" aria-hidden="true"><path d="M6.6 10.8a15.1 15.1 0 0 0 6.6 6.6l2.2-2.2a1 1 0 0 1 1-.25 11.4 11.4 0 0 0 3.6.57 1 1 0 0 1 1 1V20a1 1 0 0 1-1 1A17 17 0 0 1 3 4a1 1 0 0 1 1-1h3.5a1 1 0 0 1 1 1c0 1.25.2 2.45.57 3.57a1 1 0 0 1-.25 1z"/></svg>
        (908) 000 - 1111
      </p>
      <p class="line">
        <svg viewBox="0 0 24 24" aria-hidden="true"><path d="M2 5h20v14H2z M2 5l10 8 10-8" /></svg>
        email@domainname.com
      </p>
    </div>
    <div class="brand"><span class="brand-dot"></span>Sunvale Oil &amp; Gas</div>
    <div class="edge-rule"></div>
    <div class="edge-band"></div>
    <div class="web-tab">www.websitename.com</div>
  </section>

  <section class="card card-back" aria-label="Business card back">
    <div class="brand"><span class="brand-dot"></span>Sunvale Oil &amp; Gas</div>
  </section>
</body>
</html>
```